Real Estate Valuation Services

format
A5 portrait, look at the picture
Double-sided: Front = visual & emotional, Back = informative & structured.
goal
Highlight the free hedonic property valuation as the main offer.
Build trust by presenting the company as an exclusive, family-owned real estate firm with local roots in Meilen/ZH.
Communicate the USP “Everything from one source” clearly – from valuation to notary support and tax guidance.
Target audience
Homeowners in the Lake Zurich region considering selling their property.
Clients who value exclusivity, professionalism, and personal service.
Design style
Modern, clean, elegant – plenty of white space. Look at the website: https://brunnhofwohnen.ch/
Tone: Professional, trustworthy, exclusive – not like a mass-market flyer.
If possible, the text should be in German. Contact details must be included:
info@brunnhofwohnen.ch
+41 77 562 18 04
Target Market(s)
property owner
Industry/Entity Type
real estate
Look and feel

```html
<!DOCTYPE html>
<html lang="de">
<head>
<meta charset="utf-8">
<title>Brunnhof Wohnen – Kostenlose Immobilienbewertung</title>
<link href="https://fonts.googleapis.com/css2?family=Montserrat:wght@400;500;600;700;800&display=swap" rel="stylesheet">
<style>
  :root{
    --bg:#d0d0d0;
    --white:#ffffff;
    --green:#5a9e2a;
    --green-dark:#3f8a2a;
    --green-light:#d6e7c3;
    --text:#555555;
    --text-dark:#3c3c3c;
    --muted:#b8b8b8;
    --rule:#cfcfcf;
  }
  *{box-sizing:border-box;margin:0;padding:0}
  html,body{width:1200px;height:1200px;overflow:hidden;background:var(--bg);font-family:"Montserrat",sans-serif}
  .card{position:absolute;left:245px;width:709px;height:501px;overflow:hidden;background:var(--white)}
  .card--front{top:79px}
  .card--back{top:633px}

  /* front */
  .front-photo{position:absolute;inset:0;background:
      linear-gradient(180deg,#e8ecef 0%,#8fb8de 18%,#a9c9e6 38%,#6e9a4c 52%,#9c8a74 68%,#8b7a68 80%,#6a8a40 100%)}
  .front-shade{position:absolute;left:0;right:0;bottom:0;height:210px;
      background:linear-gradient(180deg,rgba(90,158,42,0) 0%,rgba(90,158,42,.85) 40%,var(--green) 60%)}
  .brand{color:var(--green-dark);font-weight:700;letter-spacing:.2px;white-space:nowrap}
  .front-brand{position:absolute;right:38px;top:62px;font-size:30px}
  .front-title{position:absolute;left:0;right:0;top:351px;text-align:center;color:var(--white);font-weight:800;font-size:33px;letter-spacing:.2px}
  .front-sub{position:absolute;left:0;right:0;top:395px;text-align:center;color:var(--white);font-weight:400;font-size:18.5px;line-height:22px;letter-spacing:.4px}
  .front-rule{position:absolute;left:25px;right:25px;top:458px;height:1px;background:rgba(255,255,255,.75)}
  .front-footer{position:absolute;left:25px;right:25px;top:471px;display:flex;font-size:10.5px;color:var(--white)}
  .front-footer .cta{font-weight:700;flex:1}
  .front-footer span+span{margin-left:15px}

  /* back */
  .accent-bar{position:absolute;left:0;top:0;width:25px;height:88px;background:var(--green)}
  .back-brand-box{position:absolute;left:560px;top:12px;width:135px;height:60px;background:var(--white);display:flex;align-items:center;justify-content:center;text-align:center}
  .back-brand{font-size:19px;line-height:21px;white-space:normal}
  .back-title{position:absolute;left:45px;top:33px;color:var(--green);font-weight:700;font-size:25.5px;line-height:31px;letter-spacing:.2px}
  .back-intro{position:absolute;left:45px;top:99px;width:430px;color:var(--text);font-size:11.6px;line-height:16.5px}
  .services{position:absolute;left:45px;top:143px;width:278px;list-style:none}
  .services li{position:relative;height:26px;padding-left:13px;line-height:26px;font-size:13.8px;font-weight:600;color:var(--text-dark);border-bottom:1px solid var(--rule)}
  .services li:last-child{border-bottom:none}
  .services li svg{position:absolute;left:0;top:10px}
  .usp{position:absolute;left:46px;top:253px;width:320px;border-top:1px solid var(--green-light);border-bottom:1px solid var(--green-light);padding:7px 0 8px}
  .usp h3{color:var(--green);font-size:17.5px;font-weight:700;line-height:21px}
  .usp p{color:var(--text);font-size:11.6px;line-height:14.5px;width:270px}
  .values{position:absolute;left:46px;top:329px;color:var(--muted);font-size:18.5px;font-weight:700;white-space:nowrap}
  .values i{display:inline-block;width:6px;height:6px;border-radius:50%;background:var(--green);margin:0 6px;vertical-align:-1px}
  .contact-band{position:absolute;left:0;top:358px;width:540px;height:143px;
      background:linear-gradient(90deg,#3f9a2a 0%,#5aa638 45%,#4a9a30 70%,#6fb04a 100%)}
  .contact-title{position:absolute;left:45px;top:372px;color:var(--white);font-weight:700;font-size:15px;line-height:18.5px}
  .contact-list{position:absolute;left:44px;top:425px;list-style:none;color:var(--white);font-size:11px}
  .contact-list li{height:21.5px}
  .contact-list b{font-weight:700}
  .portrait{position:absolute;left:506px;top:180px;width:203px;height:321px;
      background:linear-gradient(180deg,#f4f4f4 0%,#e2d2c4 35%,#2a2a2a 70%,#1e1e1e 100%)}
</style>
</head>
<body>

<section class="card card--front">
  <div class="front-photo" role="img" aria-label="Foto einer sonnigen Holzterrasse mit Rattanmöbeln, Blumen und Blick über Dächer auf den Zürichsee und die Berge"></div>
  <div class="front-shade"></div>
  <div class="brand front-brand">Brunnhof Wohnen</div>
  <h1 class="front-title">Kostenlose Immobilienbewertung</h1>
  <p class="front-sub">Alles aus einer Hand – von der Bewertung bis zum Notar<br>&amp; zur Steuerberatung.</p>
  <div class="front-rule"></div>
  <div class="front-footer">
    <span class="cta">Vereinbaren Sie noch heute Ihre kostenlose Bewertung</span>
    <span>Tel: +41 77 562 18 04</span>
    <span>Mail: info@brunnhofwohnen.ch</span>
  </div>
</section>

<section class="card card--back">
  <div class="accent-bar"></div>
  <div class="back-brand-box"><div class="brand back-brand">Brunnhof<br>Wohnen</div></div>
  <h2 class="back-title">Ihr exklusiver Immobilienpartner<br>in der Region Zürichsee</h2>
  <p class="back-intro">Als familiengeführtes Unternehmen mit Wurzeln in Meilen bieten wir Ihnen persönliche Betreuung, Diskretion und höchste Professionalität.</p>
  <ul class="services">
    <li><svg width="8" height="7" viewBox="0 0 8 7"><path d="M0.5 3.5 L3 6 L7.5 0.8" fill="none" stroke="#5a9e2a" stroke-width="1.3"/></svg>Immobilienbewertung</li>
    <li><svg width="8" height="7" viewBox="0 0 8 7"><path d="M0.5 3.5 L3 6 L7.5 0.8" fill="none" stroke="#5a9e2a" stroke-width="1.3"/></svg>Verkaufsstrategie &amp; Vermarktung</li>
    <li><svg width="8" height="7" viewBox="0 0 8 7"><path d="M0.5 3.5 L3 6 L7.5 0.8" fill="none" stroke="#5a9e2a" stroke-width="1.3"/></svg>Notariats &amp; Vertragsbegleitung</li>
    <li><svg width="8" height="7" viewBox="0 0 8 7"><path d="M0.5 3.5 L3 6 L7.5 0.8" fill="none" stroke="#5a9e2a" stroke-width="1.3"/></svg>Steuerberatung</li>
  </ul>
  <div class="usp">
    <h3>Alles aus einer Hand</h3>
    <p>von der Bewertung über den Verkauf bis zur steuerlichen Beratung.</p>
  </div>
  <div class="values">Exklusiv<i></i>Professionell<i></i>Persönlich</div>
  <div class="contact-band" role="img" aria-label="Grün eingefärbtes Foto einer hügeligen Landschaft mit Wohnhaus"></div>
  <p class="contact-title">Kontaktieren Sie uns für Ihre kostenlose<br>Immobilienbewertung.</p>
  <ul class="contact-list">
    <li><b>Tel:</b> +41 77 562 18 04</li>
    <li><b>Mail:</b> info@brunnhofwohnen.ch</li>
    <li><b>Web:</b> brunnhofwohnen.ch</li>
  </ul>
  <div class="portrait" role="img" aria-label="Porträtfoto einer Beraterin im dunklen Blazer"></div>
</section>

</body>
</html>
```